Business card for a plastic surgeon

i need a business card for a plastic surgeon. I have two adresses. The card should communicate safety, simmetry, beauty and with soft colors.
What i want in the card:
- my logo: Letters "R"and "T" (picture uploaded)
- my name: Rodrigo Tavernelli
- my registration: CRM 527 319
- my adresses and phone numbers (2):
- Av Dr Bento Arruda, 2730, sala 408 - Vila Serena | São Paulo/ SP - Phone: 11 4721-6350
- Al. Itaquera, 61, 3 andar - Jardim Aurora | Barueri/ SP - Phone: 11 5038-2917

- my social network: site, facebook and instagram

Target Market(s)

people (95% girls and women) that want cosmetic procedures and plastic surgery

Industry/Entity Type

Business

Contact Information for Business Card

The card should communicate safety, simmetry, beauty and with soft colors.
Beige, brown, gray, rosy are some options. Color is free

Font styles to use
Serif

Requirements
Must have
• - my logo: Letters "R"and "T" (picture uploaded)
• - my name: Rodrigo Tavernelli
• - my registration: CRM 527 319
• - my adresses and phone numbers (2):
• - Av Dr Bento Arruda, 2730, sala 408 - Vila Serena | São Paulo/ SP - Phone: 11 4721-6350
• - Al. Itaquera, 61, 3 andar - Jardim Aurora | Barueri/ SP - Phone: 11 5038-2917
• - my social network: site, facebook and instagram
Should not have
• other images (only my logo)

```html
<!DOCTYPE html>
<html lang="pt-BR">
<head>
<meta charset="utf-8">
<title>Dr. Rodrigo Tavernelli — Cartão de visita</title>
<link rel="stylesheet" href="https://fonts.googleapis.com/css2?family=Cormorant+Garamond:wght@500;600&family=Lato:wght@400&display=swap">
<style>
  :root {
    --bg: #2a2a2b;
    --card: #1d1c1b;
    --tan: #b5937b;
    --ivory: #f1eee9;
    --grey: #b8b4ae;
    --serif: "Cormorant Garamond", Georgia, serif;
    --sans: "Lato", Arial, sans-serif;
  }
  * { box-sizing: border-box; margin: 0; padding: 0; }
  html, body { width: 1200px; height: 900px; overflow: hidden; background: var(--bg); }
  .canvas { position: relative; width: 1200px; height: 900px; }
  .card {
    position: absolute; left: 260px; width: 680px; height: 390px;
    background: var(--card); box-shadow: 0 10px 30px rgba(0,0,0,.45);
  }
  .card--front { top: 45px; }
  .card--back { top: 465px; }

  /* front */
  .monogram {
    position: absolute; top: 70px; left: 0; right: 0; text-align: center;
    font-family: var(--serif); font-weight: 500; font-size: 110px; line-height: 1;
    color: var(--tan); letter-spacing: -4px;
  }
  .front-name {
    position: absolute; top: 250px; left: 0; right: 0; text-align: center;
    font-family: var(--serif); font-weight: 600; font-size: 34px;
    letter-spacing: 4px; color: var(--ivory);
  }
  .front-title {
    position: absolute; top: 298px; left: 0; right: 0; text-align: center;
    font-family: var(--serif); font-weight: 500; font-size: 19px;
    letter-spacing: 4px; color: var(--ivory);
  }

  /* back */
  .social { position: absolute; top: 52px; right: 98px; display: flex; gap: 10px; }
  .social__dot { width: 28px; height: 28px; border-radius: 50%; background: var(--tan); }
  .website {
    position: absolute; top: 96px; right: 40px;
    font-family: var(--serif); font-weight: 500; font-size: 20px; letter-spacing: 2px;
    color: var(--tan);
  }
  .website span { color: var(--ivory); }
  .back-name {
    position: absolute; top: 150px; left: 60px;
    font-family: var(--serif); font-weight: 500; font-size: 34px; color: var(--tan);
  }
  .back-role {
    position: absolute; top: 196px; left: 60px;
    font-family: var(--serif); font-weight: 500; font-size: 21px; color: var(--ivory); letter-spacing: .5px;
  }
  .rule { position: absolute; top: 232px; left: 60px; right: 40px; height: 2px; background: var(--tan); }
  .office { position: absolute; font-family: var(--sans); font-size: 16px; line-height: 1.5; color: var(--grey); font-style: normal; }
  .office__label { font-size: 18px; color: var(--tan); letter-spacing: .5px; }
  .office--aurora { top: 248px; left: 60px; }
  .office--serena { top: 282px; right: 40px; text-align: right; }
</style>
</head>
<body>
<main class="canvas">
  <section class="card card--front">
    <div class="monogram">RT</div>
    <p class="front-name">DR. RODRIGO TAVERNELLI</p>
    <p class="front-title">CIRURGIÃO PLÁSTICO</p>
  </section>

  <section class="card card--back">
    <div class="social"><span class="social__dot"></span><span class="social__dot"></span></div>
    <p class="website">DRTAVERNELLI<span>.COM.BR</span></p>
    <h1 class="back-name">DR. Rodrigo Tavernelli</h1>
    <p class="back-role">Cirurgião Plástico | CRM 527 319</p>
    <div class="rule"></div>
    <address class="office office--aurora">
      <div class="office__label">JARDIM AURORA</div>
      <div>Al. Itaquera, 61, 3 andar</div>
      <div>11 5038-2917</div>
    </address>
    <address class="office office--serena">
      <div class="office__label">VILA SERENA</div>
      <div>Av Dr Bento Arruda, 2730, sala 408</div>
      <div>11 4721-6350</div>
    </address>
  </section>
</main>
</body>
</html>
```